120ml Jar Label — Masculine Cosmetic Foot Balm for Cracked, Hardworking Heels

We need a print-ready wraparound label for a 120ml jar — a brown/amber glass jar with a black metal screw lid (file photo attached).

--DO NOT PUT A BARCODE ON THE LABEL PLEASE--
**PLEASE READ "PIXEL HARBOUR PROJECT BRIEF FINAL.MD" IN ATTACHED FILES IF YOU ARE SUBMITTING A DESIGN.**

The label is 190mm wide × 40mm high.
We need files to be in an .ai format with a 2mm bleed at the end.
Social media handle: @tallowgatenz (facebook, instagram and tiktok)

Tallow Gate is a New Zealand foot-care brand making practical, no-nonsense products for hardworking men whose jobs wreck their feet. Our flagship product, Ridge Mender Balm, helps fix thick, cracked, hardworking skin.

Brand color scheme and overview is all in the brief file. You may add some brand aligned colors outside of the specified hex codes as you see fit to make a great design. Feel free to remove the "Tallow Gate" text from the logo so Tallow Gate is not doubled up on the front of the label

The tone we want: direct, rugged, and credible — like a workwear brand, not a spa brand. Most cracked-heel products on the market lean soft and feminine; we want to stand apart by looking like a serious fix for a real problem, made in New Zealand.

Full legal requirements for New Zealand cosmetic labelling (ingredients, directions, net contents, origin, etc.) are listed in the attached brief document — these are non-negotiable and must stay legible.

Please see the label attached "Label spacing guide" for this project's rough spacing guide. This label is the same size and sits well on the jar. This label doesn't need to be spaced quite as much as the Brisko Label

I want to run the design for a week - I feel 7 days is a good amount of time for designers to see the work, digest the brief and create something remarkable and memorable for Tallow Gate.

Target Market(s)

Working men in New Zealand whose jobs or lifestyle put heavy wear on their feet — tradies, farmers, hospital/shift workers, hunters, and outdoors people. Practical, value-driven buyers rather than luxury skincare shoppers.

Industry/Entity Type

Beauty / Health & Wellness / Cosmetics

Font styles to use
Sans Serif
Other font styles liked:
• Montserrat (bold, headings), Inter (regular, body)

Colors
00AB8E
00BBA5
67D7C9
C6EFE9
E9F9F6
FFC000
F8CF3A
FAE287
FDF2CF
FEFAEE

Requirements
Must have
• All NZ cosmetic labelling requirements from the attached brief (product name, tag line, net contents, ingredients, directions, storage, made in NZ) — legible and complete, not omitted for aesthetics Fits 190mm × 40mm wraparound format for a 120ml brown jar with black lid Uses our existing brand colors: Deep Olive #3C4A34, Bone White #F4EFE6, Terracotta Clay #C1683D, and Warm Grey #4A4540 (exact palette in attached brief) Uses Montserrat (headings) and Inter (body) or close equivalents Incorporates our existing shield-and-wing logo (attached) Brand name and product name clearly readable from a normal shelf/bathroom-cabinet distance
Nice to have
• A style that could extend into a hero/product photo later, similar to the NZ-hills-backdrop look on our website (screenshot attached) — not required for the label itself, just good to keep in mind Original icon work (e.g. a small soak/apply/sock icon set) if it fits the rugged brand feel A design that could work as a small back-label/wraparound split if the front can't fit everything at a readable size
Should not have
• No pastel colors, floral motifs, or delicate script fonts — this should never look like spa/luxury skincare. Don't introduce new brand colors outside the palette provided other than black.

```html
<!DOCTYPE html>
<html lang="en">
<head>
<meta charset="utf-8">
<title>Tallow Gate — Ridge Mender Balm Label</title>
<link href="https://fonts.googleapis.com/css2?family=Montserrat:wght@600;700;800&family=Inter:wght@400;600;700&display=swap" rel="stylesheet">
<style>
  :root {
    --page: #1c1b1a;
    --olive-deep: #27301f;
    --olive: #3c4a34;
    --olive-light: #55664a;
    --bone: #f4efe6;
    --clay: #c1683d;
    --warm-grey: #4a4540;
    --white: #ffffff;
  }
  * { box-sizing: border-box; margin: 0; padding: 0; }
  html, body { width: 1200px; height: 900px; overflow: hidden; }
  body {
    background: var(--page);
    font-family: "Inter", sans-serif;
    color: var(--bone);
  }
  .label {
    position: absolute;
    left: 30px; top: 330px;
    width: 1140px; height: 240px;
    background: var(--olive-deep);
    display: grid;
    grid-template-columns: 380px 380px 380px;
  }
  .panel { position: relative; padding: 22px 26px; }

  /* back-left: directions */
  .directions h3, .ingredients h3 {
    font-family: "Montserrat", sans-serif;
    font-weight: 800;
    font-size: 13px;
    letter-spacing: 0.5px;
    margin-bottom: 4px;
  }
  .body-copy {
    font-size: 10.5px;
    line-height: 1.45;
    text-align: justify;
  }
  .storage {
    margin-top: 10px;
    font-size: 10.5px;
    font-weight: 600;
    line-height: 1.45;
    text-align: justify;
    letter-spacing: 0.4px;
  }
  .icon-row {
    display: flex;
    justify-content: center;
    gap: 10px;
    margin-top: 12px;
  }
  .icon-row svg { width: 30px; height: 30px; }
  .skin-types {
    text-align: center;
    font-family: "Montserrat", sans-serif;
    font-weight: 700;
    font-size: 11.5px;
    margin-top: 6px;
  }
  .safety {
    text-align: center;
    font-size: 8.5px;
    font-weight: 700;
    margin-top: 6px;
    letter-spacing: 0.3px;
  }

  /* front */
  .front {
    text-align: center;
    padding: 0;
    overflow: hidden;
  }
  .front .hills {
    position: absolute; inset: 0;
    background:
      linear-gradient(180deg, var(--olive) 0%, var(--olive-light) 35%, var(--olive) 60%, var(--olive-deep) 100%);
  }
  .front .content { position: relative; padding-top: 20px; }
  .brand-mark {
    display: inline-flex; align-items: center; gap: 6px;
    font-family: "Montserrat", sans-serif;
    font-weight: 700;
    font-size: 16px;
    color: var(--bone);
    letter-spacing: 0.5px;
  }
  .brand-mark .dot {
    width: 10px; height: 10px; border-radius: 50%;
    background: var(--bone);
  }
  .brand-origin {
    font-family: "Montserrat", sans-serif;
    font-weight: 700;
    font-size: 10px;
    color: var(--bone);
    margin-top: 1px;
  }
  .product-name {
    font-family: "Montserrat", sans-serif;
    font-weight: 800;
    font-size: 33px;
    line-height: 1.05;
    color: #e6e2da;
    margin-top: 10px;
    letter-spacing: 0.5px;
  }
  .tagline {
    font-family: "Inter", sans-serif;
    font-weight: 600;
    font-size: 15px;
    color: var(--clay);
    margin-top: 6px;
    letter-spacing: 0.6px;
  }
  .net {
    font-family: "Montserrat", sans-serif;
    font-weight: 700;
    font-size: 12px;
    margin-top: 5px;
  }

  /* back-right: ingredients */
  .ingredients .body-copy { font-size: 9.5px; }
  .origin {
    font-family: "Montserrat", sans-serif;
    font-weight: 700;
    font-size: 13px;
    text-align: center;
    margin-top: 6px;
  }
  .links { font-size: 9.5px; line-height: 1.4; margin-top: 3px; }
  .compliance {
    display: flex; align-items: center; gap: 10px;
    margin-top: 8px;
  }
  .badge {
    width: 32px; height: 32px; border-radius: 50%;
    border: 1.5px solid var(--bone);
  }
  .batch { font-size: 10px; line-height: 1.7; margin-left: 6px; }
  .batch-box {
    width: 92px; height: 36px;
    background: var(--white);
    margin-left: auto;
  }
</style>
</head>
<body>
  <main class="label">
    <section class="panel directions">
      <h3>DIRECTIONS:</h3>
      <p class="body-copy">Apply generously to clean, dry feet, focusing on heels and thick or cracked areas. For cracked heels, wear our moisture-locking socks overnight. Use daily.</p>
      <p class="storage">KEEP OUT OF DIRECT SUNLIGHT. BEST USED WITHIN SIX MONTHS OF OPENING.</p>
      <div class="icon-row" aria-hidden="true">
        <svg viewBox="0 0 30 30"><circle cx="15" cy="15" r="13" fill="none" stroke="var(--bone)" stroke-width="1.5"/><path d="M15 8c-3 4-5 7-5 9a5 5 0 0 0 10 0c0-2-2-5-5-9z" fill="var(--bone)"/></svg>
        <svg viewBox="0 0 30 30"><circle cx="15" cy="15" r="13" fill="none" stroke="var(--bone)" stroke-width="1.5"/><path d="M15 8c-3 4-5 7-5 9a5 5 0 0 0 10 0c0-2-2-5-5-9z" fill="var(--bone)"/></svg>
        <svg viewBox="0 0 30 30"><circle cx="15" cy="15" r="13" fill="none" stroke="var(--bone)" stroke-width="1.5"/><path d="M15 8c-3 4-5 7-5 9a5 5 0 0 0 10 0c0-2-2-5-5-9z" fill="var(--bone)"/></svg>
        <svg viewBox="0 0 30 30"><circle cx="15" cy="15" r="13" fill="none" stroke="var(--bone)" stroke-width="1.5"/><path d="M15 8c-3 4-5 7-5 9a5 5 0 0 0 10 0c0-2-2-5-5-9z" fill="var(--bone)"/></svg>
        <svg viewBox="0 0 30 30"><circle cx="15" cy="15" r="13" fill="none" stroke="var(--bone)" stroke-width="1.5"/><path d="M15 8c-3 4-5 7-5 9a5 5 0 0 0 10 0c0-2-2-5-5-9z" fill="var(--bone)"/></svg>
      </div>
      <p class="skin-types">FOR ALL SKIN TYPES</p>
      <p class="safety">SAFE &amp; NON TOXIC | EXTERNAL USE ONLY</p>
    </section>

    <section class="panel front">
      <div class="hills" role="img" aria-label="Rolling New Zealand hills landscape in deep olive tones"></div>
      <div class="content">
        <div class="brand-mark"><span class="dot"></span>TALLOW GATE</div>
        <div class="brand-origin">NZ</div>
        <h1 class="product-name">RIDGE MENDER<br>BALM</h1>
        <p class="tagline">For Hardworking Soles</p>
        <p class="net">120 ML</p>
      </div>
    </section>

    <section class="panel ingredients">
      <h3>INGREDIENTS:</h3>
      <p class="body-copy">Shea Butter, Beef Tallow, Beeswax, Grape Seed Oil, Vegetable Glycerin, Lanolin, Panthenol, Gluconolactone, Sodium Benzoate, Allantoin, Manuka Honey, Vitamin E, Tea Tree Essential Oil, Lemon Myrtle Essential Oil, Rosemary Oleoresin Extract.</p>
      <p class="origin">Made in New Zealand</p>
      <p class="links">https://www.tallowgate.co.nz/<br>@tallowgatenz</p>
      <div class="compliance">
        <span class="badge" aria-hidden="true"></span>
        <span class="badge" aria-hidden="true"></span>
        <p class="batch">Batch No.<br>Best Before:</p>
        <span class="batch-box"></span>
      </div>
    </section>
  </main>
</body>
</html>
```